High Quality Business card for Property Management Agency - Super Classy and professional design

High Quality Business card design.

We need a business card designed for our Property Management Agency.
We are located on Sydney's Northern Beaches and manage beautiful properties along the beach and harbor.
We need a design that oozes modern, classy and professional.
I would like it to be double sided with contact details and logo on the front and just the logo on the back.

I need a print ready PDF version of the file as well as an editable photoshop (PSD) version of the file.

Logo and information details attached.

Target Market(s)

Property owners/investors, Male and Female Aged 28-65

Industry/Entity Type

Real Estate

Contact Information for Business Card

Tom Harlow
Tel: 0437 216 590
Email: tom@harlowestates.com.au
Website: www.harlowestates.com.au
Address: Level 2, 17 Kestrel Rd, Wendale NSW 2081

Font styles to use
Sans Serif

Requirements
Must have
• - Logo front and back
• - Business card details listed above and attached
• - Colour
Nice to have
• Sleek and professional

```html
<!DOCTYPE html>
<html lang="en">
<head>
<meta charset="utf-8">
<title>Harlow Estates – Business Card</title>
<link rel="stylesheet" href="https://fonts.googleapis.com/css2?family=Arimo:wght@400;700&family=Tinos:wght@700&display=swap">
<style>
  :root {
    --stage: #e6e7e9;
    --card: #ffffff;
    --card-edge: #f1f2f3;
    --ink: #1e1f21;
    --ink-soft: #3a3b3d;
    --teal: #2e9c9e;
    --teal-deep: #23868a;
    --white: #ffffff;
  }
  * { box-sizing: border-box; margin: 0; padding: 0; }
  html, body {
    width: 1200px;
    height: 997px;
    overflow: hidden;
    background: var(--stage);
    font-family: "Arimo", Arial, sans-serif;
    color: var(--ink);
  }
  .canvas {
    position: relative;
    width: 1200px;
    height: 997px;
  }
  .card {
    position: absolute;
    left: 260px;
    width: 680px;
    height: 388px;
    border-radius: 20px;
    background: linear-gradient(180deg, var(--card) 0%, var(--card-edge) 100%);
    box-shadow: 0 14px 34px rgba(0,0,0,0.18), 0 2px 6px rgba(0,0,0,0.08);
    overflow: hidden;
  }
  .card--back { top: 72px; }
  .card--front { top: 530px; }

  /* brand mark: name + one plain square */
  .brand {
    display: flex;
    align-items: center;
    gap: 12px;
    font-family: "Arimo", Arial, sans-serif;
    font-weight: 700;
    color: var(--ink);
    letter-spacing: 0.02em;
    white-space: nowrap;
  }
  .brand__square {
    display: block;
    background: var(--teal);
    flex: none;
  }
  .card--back .brand {
    position: absolute;
    left: 50%;
    top: 50%;
    transform: translate(-50%, -50%);
    font-size: 52px;
  }
  .card--back .brand__square { width: 30px; height: 30px; }
  .card--front .brand {
    position: absolute;
    right: 40px;
    top: 52px;
    font-size: 29px;
  }
  .card--front .brand__square { width: 18px; height: 18px; }

  .holder {
    position: absolute;
    left: 64px;
    top: 116px;
  }
  .holder__name {
    font-family: "Tinos", "Times New Roman", serif;
    font-weight: 700;
    font-size: 26px;
    letter-spacing: 0.06em;
    color: var(--ink);
    text-transform: uppercase;
    line-height: 1;
  }
  .holder__role {
    margin-top: 5px;
    font-size: 16px;
    color: var(--teal);
    letter-spacing: 0.02em;
  }

  .icon-tab {
    position: absolute;
    left: 0;
    top: 222px;
    width: 38px;
    height: 120px;
    background: var(--teal);
    border-radius: 0 10px 10px 0;
  }
  .icon-tab svg {
    position: absolute;
    left: 11px;
    width: 16px;
    height: 16px;
  }
  .icon-tab .icon--phone { top: 16px; }
  .icon-tab .icon--mail { top: 52px; }
  .icon-tab .icon--home { top: 88px; }

  .contact {
    position: absolute;
    left: 64px;
    top: 236px;
    list-style: none;
    font-size: 15px;
    color: var(--ink-soft);
    letter-spacing: 0.01em;
  }
  .contact li { height: 36px; line-height: 18px; }

  .web-band {
    position: absolute;
    right: 0;
    bottom: 0;
    width: 380px;
    height: 72px;
  }
  .web-band__url {
    position: absolute;
    right: 26px;
    bottom: 14px;
    font-size: 16px;
    color: var(--white);
    letter-spacing: 0.03em;
  }
</style>
</head>
<body>
<main class="canvas">

  <section class="card card--back" aria-label="Business card, back">
    <div class="brand"><span class="brand__square"></span>HARLOW ESTATES</div>
  </section>

  <section class="card card--front" aria-label="Business card, front">
    <div class="brand"><span class="brand__square"></span>HARLOW ESTATES</div>

    <div class="holder">
      <p class="holder__name">Tom Harlow</p>
      <p class="holder__role">Managing Partner</p>
    </div>

    <div class="icon-tab" aria-hidden="true">
      <svg class="icon--phone" viewBox="0 0 16 16"><path fill="#fff" d="M3.5 1.5c.6-.3 1.2 0 1.5.5l1.2 2.2c.3.5.1 1.1-.3 1.4l-.9.7c.7 1.5 1.9 2.7 3.4 3.4l.7-.9c.3-.4.9-.6 1.4-.3l2.2 1.2c.5.3.8.9.5 1.5l-.6 1.2c-.4.8-1.3 1.2-2.2 1C6.1 12.6 3.4 9.9 2.6 5.6c-.2-.9.2-1.8 1-2.2z"/></svg>
      <svg class="icon--mail" viewBox="0 0 16 16"><rect x="1.5" y="3.5" width="13" height="9" rx="1" fill="#fff"/><path d="M2 4.2l6 4.6 6-4.6" fill="none" stroke="#2e9c9e" stroke-width="1.2"/></svg>
      <svg class="icon--home" viewBox="0 0 16 16"><path fill="#fff" d="M8 1.8L1 8h2v6h4v-4h2v4h4V8h2z"/></svg>
    </div>

    <ul class="contact">
      <li>0437 216 590</li>
      <li>tom@harlowestates.com.au</li>
      <li>Level 2, 17 Kestrel Rd, Wendale NSW 2081</li>
    </ul>

    <svg class="web-band" viewBox="0 0 380 72" preserveAspectRatio="none" aria-hidden="true">
      <path d="M0 72 C 22 72, 22 26, 58 26 L 380 26 L 380 72 Z" fill="#2e9c9e"/>
      <path d="M0 72 C 22 72, 22 26, 58 26 L 380 26 L 380 30 L 60 30 C 28 30, 28 72, 6 72 Z" fill="#23868a" opacity="0.55"/>
    </svg>
    <p class="web-band__url">www.harlowestates.com.au</p>
  </section>

</main>
</body>
</html>
```